Etiketten-Design für Nahrungsergänzungsmittel
Zielgruppe
Die Firma vertreibt Nahrungsergänzungsmittel, gesunde Lebensmittel, Lifestyle und Wellnessprodukte. Dies vor allem im Fitness und Sport Bereich. Die Marke und das entsprechende Logo sollen auf eine jüngere Zielgruppe 25+ ausgerichtet sein. Personen die für Ihren Körper und Gesundheit Sport treiben und zusätzlich Unterstützung benötigen. Die Produkte werden über Pictoloop durch eine Fitnesstrainerin beworben, und hauptsächlich über Varuno vertrieben. Produkte sind z. B. Produkte zur Ausdauersteigerung, verbesserte Konzentration, Schlaf, Stressbewältigung. Protein Shakes oder Vitamine für Veganer. No gos, Diät Produkte 5kg in 3 Tagen, Potenzsteigerung, Brustvergrößerung oder ähnliches.
Aufgabenstellung
Das Etikett wird auf einen wiederverschließbaren schwarz matten Kraftpapier Beutel im Format 28x20cm aufgebracht. Der Beutel und auch das Etikett sind kompostierbar, sieht aber beides hochwertig aus. Das Produkt ist ein veganes Proteinpulver zum anrühren mit Wasser oder Milchalternative. Einen ersten Entwurf habe ich hochgeladen.

```html
<!DOCTYPE html>
<html lang="de">
<head>
<meta charset="utf-8">
<title>LIORA – Veganer Protein Shake Etikett</title>
<link href="https://fonts.googleapis.com/css2?family=Exo+2:ital,wght@1,800;1,900&family=Quicksand:wght@500;700&display=swap" rel="stylesheet">
<style>
  :root {
    --bg: #2b2b2b;
    --label: #222222;
    --label-deep: #1c1c1c;
    --teal: #0aa5a0;
    --teal-light: #14b8b2;
    --white: #ffffff;
    --line: #e8e8e8;
    --text: #f2f2f2;
  }
  * { margin: 0; padding: 0; box-sizing: border-box; }
  html, body { width: 853px; height: 1200px; overflow: hidden; }
  body {
    background: var(--bg);
    font-family: "Quicksand", sans-serif;
    color: var(--text);
    position: relative;
  }
  .label {
    position: absolute;
    top: 323px;
    width: 395px;
    height: 554px;
    border: 3px solid var(--white);
    border-radius: 16px;
    background: var(--label);
    overflow: hidden;
  }
  .label--front { left: 22px; }
  .label--back { left: 436px; }
  .label__shapes { position: absolute; inset: 0; width: 100%; height: 100%; }

  /* Front */
  .brand {
    position: absolute;
    top: 150px; left: 0; right: 0;
    text-align: center;
    font-family: "Quicksand", sans-serif;
    font-weight: 700;
    font-size: 38px;
    letter-spacing: 2px;
    color: var(--white);
  }
  .product-title {
    position: absolute;
    top: 312px; left: 0; right: 0;
    text-align: center;
    font-family: "Exo 2", sans-serif;
    font-style: italic;
    font-weight: 900;
    line-height: 0.98;
    text-transform: uppercase;
  }
  .product-title__accent { display: block; color: var(--teal); font-size: 48px; }
  .product-title__main { display: block; color: var(--white); font-size: 46px; }

  /* Back */
  .back-content { position: absolute; left: 40px; top: 40px; width: 312px; font-size: 6.6px; line-height: 1.45; }
  .legal-name { font-weight: 700; font-size: 7.4px; line-height: 1.4; }
  .ingredients { margin-top: 8px; font-size: 6.6px; }
  table { border-collapse: collapse; width: 100%; text-align: center; }
  td, th { border: 0.8px solid var(--line); padding: 0 2px; height: 14px; font-weight: 500; }
  th { font-weight: 700; }
  .nutrition { margin-top: 11px; }
  .nutrition td.energy { height: 27px; line-height: 1.25; }
  .amino-title { margin-top: 6px; }
  .amino-title th { height: 14px; }
  .amino { margin-top: 3px; }
  .amino td { height: 13.8px; }
  .usage { position: absolute; left: 40px; top: 380px; width: 200px; font-size: 6.6px; line-height: 1.45; }
  .usage strong { font-weight: 700; }
  .usage p + p { margin-top: 3px; }
  .social {
    position: absolute; right: 128px; top: 438px;
    text-align: right; font-size: 5px; line-height: 1.5; color: var(--teal-light); font-weight: 700;
  }
  .social__handle { color: var(--white); font-size: 6.2px; display: inline-flex; align-items: center; gap: 3px; }
  .social__dot { width: 5px; height: 5px; border: 0.8px solid var(--teal-light); border-radius: 50%; display: inline-block; }
  .trainer-photo {
    position: absolute; left: 268px; top: 348px; width: 124px; height: 203px;
    background: linear-gradient(180deg, #3f6a78 0%, #4c7c8a 45%, #1e1e22 75%, #121214 100%);
    border-radius: 50px 50px 0 0;
  }
</style>
</head>
<body>

<section class="label label--front" aria-label="Vorderseite Etikett">
  <svg class="label__shapes" viewBox="0 0 395 554" preserveAspectRatio="none" aria-hidden="true">
    <polygon points="0,0 245,0 0,32" fill="#0aa5a0"/>
    <polygon points="0,300 395,232 395,554 0,554" fill="#1c1c1c"/>
    <polygon points="270,242 395,224 395,230 250,247" fill="#0aa5a0"/>
    <polygon points="0,515 135,500 0,522" fill="#0aa5a0"/>
    <polygon points="0,530 395,468 395,554 0,554" fill="#0aa5a0"/>
  </svg>
  <div class="brand">LIORA</div>
  <h1 class="product-title">
    <span class="product-title__accent">Veganer</span>
    <span class="product-title__main">Protein</span>
    <span class="product-title__main">Shake</span>
  </h1>
</section>

<section class="label label--back" aria-label="Rückseite Etikett">
  <svg class="label__shapes" viewBox="0 0 395 554" preserveAspectRatio="none" aria-hidden="true">
    <polygon points="0,300 395,232 395,554 0,554" fill="#1f1f1f"/>
    <polygon points="0,552 395,468 395,554 0,554" fill="#0aa5a0"/>
  </svg>

  <div class="back-content">
    <p class="legal-name">Getränkepulver zur Herstellung eines veganen Eiweißgetränkes mit Süßungsmittel - Geschmacksrichtung Vanille</p>
    <p class="ingredients">Zutaten: Eiweißmischung (93%) (Erbseneiweiß, Reiseiweiß, Hanfsamenpulver, Bio Kürbiskerneiweiß), Aroma, Verdickungsmittel: Xanthan, Kokosnussmilchpulver, Süßungsmittel: Sucralose</p>

    <table class="nutrition">
      <tr><th style="width:43%">Nährwertangaben pro</th><th style="width:30%">100g</th><th>Portion = 30g</th></tr>
      <tr><td>Energie</td><td class="energy">1.694 kJ /<br>401 kcal</td><td class="energy">508 kJ /<br>120 kcal</td></tr>
      <tr><td>Fett</td><td>8,3 g</td><td>2,5 g</td></tr>
      <tr><td>- davon gesättigte Fettsäuren</td><td>2,2 g</td><td>0,7 g</td></tr>
      <tr><td>Kohlenhydrate</td><td>4,0 g</td><td>1,2 g</td></tr>
      <tr><td>- davon Zucker</td><td>1,2 g</td><td>0,4 g</td></tr>
      <tr><td>Ballaststoffe</td><td>4,4 g</td><td>1,3 g</td></tr>
      <tr><td>Eiweiß</td><td>75,3 g</td><td>22,6 g</td></tr>
      <tr><td>Salz</td><td>2,15 g</td><td>0,64 g</td></tr>
    </table>

    <table class="amino-title"><tr><th>Aminosäurenprofil pro 100g Eweiß</th></tr></table>
    <table class="amino">
      <tr><td>Isoleucin</td><td>4,4 g</td><td>Tryptophan</td><td>1,1 g</td><td>Alanin</td><td>8,9 g</td></tr>
      <tr><td>Leucin</td><td>8,4 g</td><td>Valin</td><td>5,3 g</td><td>Asparaginsäure</td><td>11,1 g</td></tr>
      <tr><td>Lysin</td><td>6,7 g</td><td>Histidin</td><td>2,5 g</td><td>Glutaminsäure</td><td>17,2 g</td></tr>
      <tr><td>Methionin</td><td>1,4 g</td><td>Arginin</td><td>8,9 g</td><td>Glycin</td><td>4,2 g</td></tr>
      <tr><td>Phenylalanin</td><td>5,5 g</td><td>Tyrosin</td><td>3,8 g</td><td>Prolin</td><td>4,4 g</td></tr>
      <tr><td>Threonin</td><td>3,7 g</td><td>Cystein</td><td>1,4 g</td><td>Serin</td><td>5,1 g</td></tr>
    </table>
  </div>

  <div class="usage">
    <p><strong>Verzehrempfehlung:</strong> 30 g Pulver<br><strong>in 300 ml Wasser lösen;</strong><br>Das Produkt ist kühl, trocken und<br>dunkel zu lagern.</p>
    <p><strong>LIORA UG</strong><br>Lindenweg 12<br>70173 Musterstadt<br>info@liorashop.de</p>
    <p>Inhalt: 600g Eiweißpulver für 20 Shakes<br>Mindestens haltbar bis Ende:<br>08/2023; Losnummer: 977109</p>
  </div>

  <div class="social">
    Besucht uns auch auf Pictoloop<br>Liebe Grüße Liora<br>
    <span class="social__handle"><span class="social__dot"></span>liorabyliora</span>
  </div>

  <div class="trainer-photo" role="img" aria-label="Foto der Fitnesstrainerin in blauem Sport-Top und schwarzer Leggings"></div>
</section>

</body>
</html>
```